PostCard Design Project

I am making a mailing postcard
I am having the mailing printed using 4 color foil on certain parts.
I am looking for a design that maximizes the foil process where certain parts are done in foil to grab the customers attention (example: if there is a car on the postcard the headlights would be done in foil) .
I am targeting some industries, (auto, real estate, medical, beauty) I would like the post card to have examples of postcard ideas for 2 or 3 of these industries.
specs:
the postcard should be atleast 6.5x9 up to 8.5x11, I don't want to restrict the space for the creative as I don't want everything to look like a huge mess. both sides will be used.
the piece is a direct mail piece so it has to meet requirements of https://www.parcelvane-post.com/business/pdf/quick-reference-guide.pdf
text will be
"business with no limits, meet mailing with no addresses, gain new customers through "Whole Route Flyer Drop" reach new customers at their home without needing their address. "
I also want some current print specials I am running included.
-double your order FREE (order 500 business cards and get 1000)
-250 100lb gloss stock brochures 99.00
-business packages (cards, envelopes and letterhead) 299
-1000 flyers 140.40
-5000 postcards 179.99
A list of services
banners
booklets
brochures
business cards
calendars
catalogs
CD/DVD packages
envelopes
event tickets
flyers
hangtags
postcards
posters
presentation folders
rack cards
labels
table tents
window cling and decal
"order 24/7 orders@cardwillow.com" must be included
my logo is CardWillow will be supplied later
ive received some great designs. however Im looking for something a little more modern like some zelkor would put out. if the amount of words is too much please feel free to edit. also an idea i had for the list of services i offer is to have it transparent yet readable as the background of the postcard some small some big but covering the entire backgroud. you can then design on top of that with other thing. just an early morning thought
Reason: I have uploaded a sketch of my idea, please take time to look at it for an accurate depiction of what im looking for. feel free to add elements that make it pop off the page
Reason: We are getting close i will be providing feed back today
Business

```html
<!DOCTYPE html>
<html lang="en">
<head>
<meta charset="utf-8">
<title>CardWillow Mailing Postcard</title>
<link rel="stylesheet" href="https://fonts.googleapis.com/css2?family=PT+Sans:ital,wght@0,400;0,700;1,400;1,700&family=Zilla+Slab:wght@300;400;600&display=swap">
<style>
  :root {
    --page: #f4f4f4;
    --ink-black: #000000;
    --ink-white: #ffffff;
    --ink-dark: #1e1e1e;
    --rule: #9a9a9a;
    --gold: #d9a441;
    --gold-light: #f3dca2;
    --auto-blue: #1b75bb;
    --dent-blue: #1a75bf;
    --photo-brown: #7a4a22;
    --photo-tan: #d8a36a;
    --estate-green: #8dc63f;
    --gray-1: #8a8a8a;
    --gray-2: #a5a5a5;
    --gray-3: #c2c2c2;
    --gray-4: #d8d8d8;
    --logo-gray: #b0b0b0;
  }
  * { margin: 0; padding: 0; box-sizing: border-box; }
  html, body { width: 1200px; height: 420px; overflow: hidden; background: var(--page); }
  .canvas { position: relative; width: 1200px; height: 420px; }
  .card { position: absolute; top: 18px; width: 540px; height: 390px; overflow: hidden; }

  /* Front */
  .card--front { left: 50px; background: var(--ink-black); color: var(--ink-white); }
  .front__ornament {
    position: absolute; right: 0; top: 0; width: 210px; height: 190px;
    background: radial-gradient(circle at 100% 10%, rgba(217,164,65,.8) 0%, rgba(217,164,65,.35) 40%, rgba(0,0,0,0) 72%);
  }
  .front__headline {
    position: absolute; left: 22px; top: 16px;
    font-family: "Zilla Slab", serif; font-weight: 300;
    font-size: 43px; line-height: 47px; letter-spacing: 1px;
  }
  .front__order {
    position: absolute; left: 22px; top: 119px;
    font-family: "PT Sans", sans-serif; font-weight: 700; font-size: 17px; letter-spacing: .3px;
  }
  .sample { position: absolute; overflow: hidden; font-family: "PT Sans", sans-serif; }
  .sample--auto { left: 22px; top: 173px; width: 247px; height: 166px; background: var(--ink-white); }
  .sample--auto .sample__photo {
    position: absolute; right: 0; top: 0; width: 130px; height: 60px;
    background: linear-gradient(90deg, rgba(255,255,255,1) 0%, #b9b2a6 60%, #6c6458 100%);
  }
  .sample--auto .sample__title { position: absolute; left: 11px; top: 8px; color: var(--auto-blue); font-weight: 700; font-size: 28px; line-height: 28px; }
  .sample--auto .sample__sub { position: absolute; left: 11px; top: 36px; color: #555; font-weight: 700; font-size: 14px; }
  .sample--auto .sample__body { position: absolute; left: 11px; top: 73px; width: 76px; color: #999; font-size: 7.5px; line-height: 10px; }
  .sample--auto .sample__foot { position: absolute; left: 11px; bottom: 6px; color: #aaa; font-size: 4.5px; }

  .sample--dentist { left: 110px; top: 209px; width: 233px; height: 130px; background: var(--dent-blue); }
  .sample--dentist .sample__photo {
    position: absolute; left: 0; top: 0; width: 233px; height: 82px;
    background: linear-gradient(90deg, #4a2a10 0%, var(--photo-brown) 45%, var(--photo-tan) 75%, #f0d8b8 100%);
  }
  .sample--dentist .sample__title { position: absolute; left: 14px; top: 10px; color: var(--ink-white); font-size: 24px; }
  .sample--dentist .sample__tag { position: absolute; left: 14px; top: 38px; color: var(--ink-white); font-style: italic; font-size: 11px; }
  .sample--dentist .sample__name { position: absolute; left: 14px; top: 90px; color: var(--ink-white); font-weight: 700; font-size: 17px; line-height: 16px; }
  .sample--dentist .sample__kind { position: absolute; left: 14px; top: 106px; color: var(--ink-white); font-size: 11px; }
  .sample--dentist .sample__note { position: absolute; left: 78px; top: 92px; color: var(--ink-white); font-style: italic; font-size: 6.5px; line-height: 9px; }

  .sample--estate { left: 218px; top: 258px; width: 159px; height: 81px; background: var(--estate-green); color: var(--ink-white); }
  .sample--estate .sample__title { position: absolute; left: 10px; top: 8px; font-style: italic; font-size: 8.5px; line-height: 10px; }
  .sample--estate .sample__contact { position: absolute; left: 10px; top: 56px; font-size: 4.5px; line-height: 5.5px; color: #eaf5d8; }
  .sample--estate .sample__mark { position: absolute; left: 92px; top: 8px; width: 58px; height: 58px; background: rgba(255,255,255,.35); }

  .front__logo {
    position: absolute; left: 416px; top: 323px;
    font-family: "PT Sans", sans-serif; font-weight: 700; font-size: 19px; color: var(--ink-white);
  }

  /* Back */
  .card--back { left: 623px; background: var(--ink-white); color: var(--ink-dark); }
  .back__ornament {
    position: absolute; right: 0; top: 0; width: 150px; height: 190px;
    background: radial-gradient(circle at 65% 30%, rgba(255,255,255,.95) 0%, var(--gold-light) 28%, rgba(217,164,65,.45) 52%, rgba(255,255,255,0) 75%);
  }
  .services {
    position: absolute; left: 18px; top: 20px; width: 600px;
    font-family: "PT Sans", sans-serif; font-weight: 700; font-style: italic;
    font-size: 26px; line-height: 19px; letter-spacing: -.4px; white-space: nowrap;
  }
  .services__line { height: 19px; }
  .tone-1 { color: var(--gray-1); }
  .tone-2 { color: var(--gray-2); }
  .tone-3 { color: var(--gray-3); }
  .tone-4 { color: var(--gray-4); }
  .services__fade {
    position: absolute; left: 130px; top: 0; width: 410px; height: 175px;
    background: linear-gradient(90deg, rgba(255,255,255,0) 0%, rgba(255,255,255,.7) 50%, rgba(255,255,255,.9) 100%);
  }
  .stamp { position: absolute; left: 446px; top: 28px; width: 66px; height: 72px; border: 1px solid var(--rule); }
  .back__pitch, .specials, .back__visit {
    position: absolute; left: 18px; font-family: "Zilla Slab", serif; font-size: 12.5px; line-height: 14px;
  }
  .back__pitch { top: 172px; width: 224px; }
  .specials { top: 252px; list-style: none; }
  .back__visit { top: 339px; font-family: "PT Sans", sans-serif; font-size: 10.5px; }
  .back__visit strong { font-weight: 700; }
  .address-line { position: absolute; left: 277px; width: 235px; height: 1px; background: var(--rule); }
  .address-line--1 { top: 185px; }
  .address-line--2 { top: 218px; }
  .address-line--3 { top: 250px; }
  .address-line--4 { top: 283px; }
  .back__logo {
    position: absolute; left: 440px; top: 330px;
    font-family: "PT Sans", sans-serif; font-weight: 700; font-size: 15px; color: var(--logo-gray);
  }
</style>
</head>
<body>
<main class="canvas">

  <section class="card card--front" aria-label="Postcard front">
    <div class="front__ornament" role="img" aria-label="Gold foil ornamental pattern"></div>
    <h1 class="front__headline">LET US MAKE YOUR<br>BUSSINESS SHINE !</h1>
    <p class="front__order">order 24/7 orders@cardwillow.com</p>

    <article class="sample sample--auto">
      <div class="sample__photo" role="img" aria-label="Photo of a car"></div>
      <div class="sample__title">Auto</div>
      <div class="sample__sub">company</div>
      <p class="sample__body">Quick service and honest repairs for every car, truck and van.</p>
      <p class="sample__foot">Open daily, call us for a free estimate</p>
    </article>

    <article class="sample sample--dentist">
      <div class="sample__photo" role="img" aria-label="Photo of a smiling child"></div>
      <div class="sample__title">Smile</div>
      <div class="sample__tag">with confident</div>
      <div class="sample__name">ABC</div>
      <div class="sample__kind">dentists</div>
      <p class="sample__note">Gentle care for<br>your whole<br>family.</p>
    </article>

    <article class="sample sample--estate">
      <p class="sample__title">We are<br>real estate<br>agents</p>
      <p class="sample__contact">12 Oak Lane, City<br>000 000 000<br>www.youragent.com</p>
      <div class="sample__mark" role="img" aria-label="Hand-drawn house illustration"></div>
    </article>

    <div class="front__logo">CardWillow</div>
  </section>

  <section class="card card--back" aria-label="Postcard back">
    <div class="back__ornament" role="img" aria-label="Gold foil ornamental pattern"></div>
    <div class="services" aria-label="Services">
      <div class="services__line"><span class="tone-1">business cards</span><span class="tone-2">brochures</span><span class="tone-3">banners</span><span class="tone-4">booklets</span></div>
      <div class="services__line"><span class="tone-3">calendars</span><span class="tone-2">catalogs</span><span class="tone-3">CD/DVD packages</span></div>
      <div class="services__line"><span class="tone-1">envelopes</span><span class="tone-3">event tickets</span><span class="tone-2">flyers</span><span class="tone-3">hangtags</span></div>
      <div class="services__line"><span class="tone-1">postcards</span><span class="tone-3">posters</span><span class="tone-2">presentation folders</span></div>
      <div class="services__line"><span class="tone-2">window cling </span><span class="tone-3">and decal</span></div>
      <div class="services__line"><span class="tone-4">rack cards</span><span class="tone-3">labels</span></div>
      <div class="services__line"><span class="tone-3">table tents</span></div>
    </div>
    <div class="services__fade"></div>
    <div class="stamp"></div>

    <p class="back__pitch">business with no limits, meet mailing with no addresses, gain new customers through "Whole Route Flyer Drop" reach new customers at their home without needing their address.</p>
    <ul class="specials">
      <li>» double your order FREE</li>
      <li>» 250 100lb gloss stock brochures 99.00</li>
      <li>» business packages 299</li>
      <li>» 1000 flyers 140.40</li>
      <li>» 5000 postcards 179.99</li>
    </ul>
    <p class="back__visit">visit <strong>yourwebsite.com</strong> for more info.</p>

    <div class="address-line address-line--1"></div>
    <div class="address-line address-line--2"></div>
    <div class="address-line address-line--3"></div>
    <div class="address-line address-line--4"></div>

    <div class="back__logo">CardWillow</div>
  </section>

</main>
</body>
</html>
```